Design an eye-catching A5 flyer for print to attract dog owners attention

PawHarbor is a UK based online community that is free for dog owners. It is designed to be a dog specific version of 'Chatterly' for social networking, combined with a 'RoamRanker' concept so dog owners can discover dog friendy products and services.

I would like a design for a double sided colour A5 flyer that is print ready to leave in places like pet shops, vets, groomers etc on counters and pin boards to attract dog owners.

I want the flyer to provide information about what they can use the site for along with emphaising it is totally free and a call to action for them to sign up to use it.

To include as mandatory:
- brand logo
- app image
- website URL

Brand logo and previosuly used imagery from the website attached for use as required along with brand pantone colour references.

Text to include:

"Join PawHarbor free today and use our website or App anywhere in the UK to:

• Find dog friendly services and products from all over the UK, rated and recommended by dog owners just like you.
• Search for new dog walks all over the UK or share your favourite walks with other dog owners.
• Store your dogs’ vital information securely and all in one place via the app or website in case of an emergency.
• Everything from dog friendly pubs to emergency vets and more all in one place, completely free.
• Connect with friends and family to share pictures and chat about your dogs.

PawHarbor is run by dog owners for dog owners."

A slighty different section of the flyer I would like to include the additional wording aimed at dog related businesses as shown below. This is not a main feature of the flyer but a point of interest if they happen to pick one up:

"If you have a dog related business, or just a business that is dog friendly and want to ‘bark’ about it, sign up for a free, no obligation, 30-day trial on our website today."

```html
<!DOCTYPE html>
<html lang="en">
<head>
<meta charset="utf-8">
<title>PawHarbor A5 Flyer</title>
<link href="https://fonts.googleapis.com/css2?family=Montserrat:wght@400;500;600&family=Raleway:wght@400;500;600&display=swap" rel="stylesheet">
<style>
  :root {
    --brand-blue: #5bbcd9;
    --brand-blue-light: #a9dcec;
    --ink: #4a4a4a;
    --ink-soft: #6b6b6b;
    --rule-grey: #6a6a6a;
    --paper: #ffffff;
    --paper-fade: #ececec;
    --stage: #e6ebed;
    --grass: #5f7f3d;
    --grass-dark: #3f5a27;
    --fur: #d9b27a;
    --blossom: #e98a3a;
  }
  * { box-sizing: border-box; margin: 0; padding: 0; }
  html, body { width: 1111px; height: 1200px; overflow: hidden; }
  body {
    background: var(--stage);
    font-family: "Montserrat", "Helvetica Neue", Arial, sans-serif;
    color: var(--ink);
    position: relative;
  }
  .flyer {
    position: absolute;
    top: 240px;
    width: 510px;
    height: 721px;
    background: linear-gradient(180deg, var(--paper) 60%, var(--paper-fade) 100%);
    box-shadow: 0 6px 20px rgba(0,0,0,.18);
    overflow: hidden;
  }
  .flyer--front { left: 30px; }
  .flyer--back { left: 571px; }

  /* ---------- front ---------- */
  .hero-photo {
    position: absolute; left: 0; top: 0; width: 510px; height: 490px;
    background:
      radial-gradient(ellipse 40% 35% at 55% 45%, var(--fur) 0%, rgba(217,178,122,0) 70%),
      radial-gradient(ellipse 90% 30% at 50% 95%, var(--blossom) 0%, rgba(233,138,58,0) 70%),
      linear-gradient(180deg, #7e9a55 0%, var(--grass) 55%, var(--grass-dark) 100%);
  }
  .brand {
    position: absolute; left: 34px; top: 110px;
    display: flex; align-items: center; gap: 8px;
    font-family: "Raleway", sans-serif; font-weight: 600;
    font-size: 26px; color: var(--brand-blue);
  }
  .brand__dot { width: 12px; height: 12px; border-radius: 50%; background: var(--brand-blue); }
  .rule-pair { position: absolute; }
  .rule-pair span { display: block; height: 4px; }
  .rule-pair .grey { background: #e8e8e8; }
  .rule-pair .blue { background: var(--brand-blue); margin-top: 5px; }
  .front-rules { left: 34px; top: 155px; width: 150px; transform: rotate(-4deg); transform-origin: left; }

  .phone {
    position: absolute;
    background: #fafafa;
    border: 3px solid #9a9a9a;
    border-radius: 18px;
    box-shadow: 0 4px 12px rgba(0,0,0,.3);
  }
  .phone__screen {
    position: absolute; background: var(--paper);
    display: flex; flex-direction: column; align-items: center;
  }
  .phone__name { font-family: "Raleway", sans-serif; font-weight: 600; color: var(--brand-blue); }
  .phone__field { width: 82%; border: 1px solid #ddd; background: #f6f6f6; }
  .phone__photo { margin-top: auto; width: 100%; background: linear-gradient(90deg, #c9b29a, #8b7c6e, #d4c1a8, #6f655c); }
  .phone__button { position: absolute; left: 50%; transform: translateX(-50%); border: 2px solid #bbb; border-radius: 50%; }
  .phone--front { left: 366px; top: 395px; width: 124px; height: 232px; }
  .phone--front .phone__screen { left: 6px; right: 6px; top: 26px; bottom: 34px; padding-top: 10px; gap: 5px; }
  .phone--front .phone__name { font-size: 15px; margin-bottom: 4px; }
  .phone--front .phone__field { height: 11px; }
  .phone--front .phone__photo { height: 42px; }
  .phone--front .phone__button { bottom: 7px; width: 20px; height: 20px; }

  .cta {
    position: absolute; left: 108px; top: 548px; width: 272px; height: 86px;
    background: var(--brand-blue); border-radius: 10px;
    box-shadow: 4px 6px 10px rgba(0,0,0,.35);
    display: flex; align-items: center; justify-content: center; text-align: center;
    color: var(--paper); font-size: 14px; font-weight: 400; line-height: 1.35;
    text-transform: uppercase; transform: rotate(-3deg);
  }
  .motto {
    position: absolute; left: 0; right: 0; text-align: center;
    font-size: 14px; font-weight: 500; line-height: 1.4; color: var(--ink);
    text-transform: uppercase;
  }
  .flyer--front .motto { top: 650px; }
  .foot-rules { left: 0; right: 0; bottom: 14px; }
  .foot-rules .grey { background: var(--rule-grey); height: 3px; }
  .foot-rules .blue { height: 3px; margin-top: 3px; }

  /* ---------- back ---------- */
  .back-top-rule { position: absolute; left: 0; right: 0; top: 16px; height: 3px; background: var(--brand-blue); }
  .dogs-strip {
    position: absolute; left: 14px; right: 14px; top: 28px; height: 128px;
    background: linear-gradient(90deg, #d8cfc4 0%, #7a6a5c 20%, #e6d2b2 38%, #3c3c3c 55%, #c9ae84 72%, #a38f7a 88%, #e5dbd0 100%);
  }
  .band { position: absolute; left: 0; top: 160px; width: 510px; height: 44px; }
  .phone--back { left: 420px; top: 170px; width: 66px; height: 124px; border-radius: 10px; border-width: 2px; }
  .phone--back .phone__screen { left: 3px; right: 3px; top: 14px; bottom: 18px; padding-top: 5px; gap: 3px; }
  .phone--back .phone__name { font-size: 8px; }
  .phone--back .phone__field { height: 5px; }
  .phone--back .phone__photo { height: 22px; }
  .phone--back .phone__button { bottom: 3px; width: 11px; height: 11px; }

  .intro {
    position: absolute; left: 28px; width: 380px; top: 222px;
    font-size: 15px; font-weight: 600; line-height: 1.35; text-transform: uppercase; color: var(--ink);
  }
  .features {
    position: absolute; left: 28px; right: 28px; top: 292px;
    list-style: none; font-size: 11px; line-height: 1.45; text-transform: uppercase; color: var(--ink-soft);
  }
  .features li { position: relative; padding-left: 16px; margin-bottom: 9px; }
  .features li::before {
    content: ""; position: absolute; left: 0; top: 5px; width: 6px; height: 6px;
    border-radius: 50%; background: var(--brand-blue);
  }
  .flyer--back .motto { top: 555px; font-size: 13px; }
  .business {
    position: absolute; left: 40px; right: 40px; top: 610px; text-align: center;
    font-size: 10.5px; line-height: 1.45; text-transform: uppercase; color: var(--ink-soft);
  }
  .business em { font-style: normal; color: var(--brand-blue); }
  .footer-bar {
    position: absolute; left: 0; right: 0; bottom: 18px; height: 26px;
    border-top: 2px solid var(--rule-grey);
    display: flex; align-items: center; justify-content: flex-end; padding-right: 24px;
    font-size: 10px; letter-spacing: .5px; color: var(--ink);
  }
  .footer-bar b { color: var(--brand-blue); font-weight: 500; }
  .footer-base { position: absolute; left: 0; right: 0; bottom: 12px; height: 3px; background: var(--brand-blue); }
</style>
</head>
<body>

  <section class="flyer flyer--front" aria-label="Flyer front">
    <div class="hero-photo" role="img" aria-label="Photo of two golden puppies sitting in grass scattered with orange flowers"></div>
    <div class="brand"><span class="brand__dot"></span>PawHarbor</div>
    <div class="rule-pair front-rules"><span class="grey"></span><span class="blue"></span></div>

    <div class="phone phone--front">
      <div class="phone__screen">
        <div class="phone__name">PawHarbor</div>
        <div class="phone__field"></div>
        <div class="phone__field"></div>
        <div class="phone__photo" role="img" aria-label="Group photo of assorted dogs"></div>
      </div>
      <div class="phone__button"></div>
    </div>

    <div class="cta">Join PawHarbor free<br>today<br>and use our website or app</div>
    <p class="motto">“PawHarbor is run by dog<br>owners for dog owners.”</p>
    <div class="rule-pair foot-rules"><span class="grey"></span><span class="blue"></span></div>
  </section>

  <section class="flyer flyer--back" aria-label="Flyer back">
    <div class="back-top-rule"></div>
    <div class="dogs-strip" role="img" aria-label="Row of assorted puppies and dogs of different breeds"></div>
    <svg class="band" viewBox="0 0 510 44" aria-hidden="true">
      <line x1="0" y1="2" x2="510" y2="2" stroke="#6a6a6a" stroke-width="2"/>
      <path d="M0 8 H510 V22 Q255 48 0 40 Z" fill="#a9dcec"/>
    </svg>

    <div class="phone phone--back">
      <div class="phone__screen">
        <div class="phone__name">PawHarbor</div>
        <div class="phone__field"></div>
        <div class="phone__field"></div>
        <div class="phone__photo" role="img" aria-label="Group photo of assorted dogs"></div>
      </div>
      <div class="phone__button"></div>
    </div>

    <h2 class="intro">Join PawHarbor free today and use our website or app anywhere in the UK to:</h2>
    <ul class="features">
      <li>Find dog friendly services and products from all over the UK, rated and recommended by dog owners just like you.</li>
      <li>Search for new dog walks all over the UK or share your favourite walks with other dog owners.</li>
      <li>Store your dogs’ vital information securely and all in one place via the app or website in case of an emergency.</li>
      <li>Everything from dog friendly pubs to emergency vets and more all in one place, completely free.</li>
      <li>Connect with friends and family to share pictures and chat about your dogs.</li>
    </ul>

    <p class="motto">“PawHarbor is run by dog owners for dog owners.”</p>
    <p class="business">“If you have a dog related business, or just a business that is dog friendly and want to ‘bark’ about it, <em>sign up for a free,</em> no obligation, 30-day trial on our website today.”</p>

    <div class="footer-bar"><b>www.pawharbor.co.uk</b></div>
    <div class="footer-base"></div>
  </section>

</body>
</html>
```